Postcard Design

Velvet Petal a Waxing Boutique - We need a postcard Front of it with a boarder done as a dainty picture frame and inside listing our services menu. We would like the picture frame to be white and the background to be a light grey and service menu writing in white as well. On back we need name, address, etc. We weould like the name to be in Turquise. Do you help design logos?
menu sheet -
Facial Services:
Brow Shaping $18
Lip - $12
Brow and Lip Combo $25
Sideburns - $12
Nose $10
Ears $10
Full Face Combo Excluding Brows $40
Full Face Combo w/ Brow Shaping $55
Lash Tint $20
Brow Tint $15
(This is to darken brows only)
Brow Shaping + Brow Tint $33

BODY WAXING :
Neck $15
Shoulders$20
Full back $45
Chest $45
(Abdomen Included)
Abdomen $15
Underarms $15
Full Arm $40
Half Arm $30
Full Leg $60
(Bikini line not included, This covers the upper thigh down to the feet and toes)
Half Leg $45
(Upper or Lower leg)
Modest Bikini - $35 Female Only
Brazilian Bikini $55 Female Only
Buttocks $20

Whats So Special About Our Pricing? Its Simple:
*Straight Forward Prices and No Tipping Policy!

Back of Card -

Velvet Petal
{Waxing Boutique}

Located in Studios Marigo
415 W. Corbin Dale Blvd
Suite 17
Rockwall, TX 75849
(972)514-2078

```html
<!DOCTYPE html>
<html lang="en">
<head>
<meta charset="utf-8">
<title>Velvet Petal – Postcard</title>
<link rel="stylesheet" href="https://fonts.googleapis.com/css2?family=Lobster+Two:ital,wght@0,700;1,700&display=swap">
<style>
  :root {
    --page: #ffffff;
    --card: #adadad;
    --ink: #ffffff;
    --mint: #7ff0be;
    --mint-soft: rgba(160, 245, 205, 0.55);
  }
  * { margin: 0; padding: 0; box-sizing: border-box; }
  html, body { width: 770px; height: 1200px; overflow: hidden; background: var(--page); }
  body {
    position: relative;
    font-family: "Lobster Two", cursive;
    font-style: italic;
    font-weight: 700;
    color: var(--ink);
  }
  .card {
    position: absolute;
    left: 0;
    width: 770px;
    height: 594px;
    background: var(--card);
  }
  .card--front { top: 0; height: 592px; }
  .card--back { top: 606px; }
  .frame { position: absolute; inset: 0; }
  .ornament {
    position: absolute;
    width: 90px;
    height: 78px;
    border-radius: 40px;
    background: var(--mint-soft);
  }
  .menu-column { position: absolute; top: 108px; list-style: none; }
  .menu-column--facial { left: 123px; }
  .menu-column--body { left: 390px; }
  .menu-heading { font-size: 22px; line-height: 28px; margin-bottom: 2px; }
  .menu-item { font-size: 15px; line-height: 22.2px; white-space: nowrap; }
  .menu-note { font-size: 11px; line-height: 20px; white-space: nowrap; }
  .menu-note--wrap { line-height: 15px; padding: 2px 0; }
  .business-name {
    position: absolute;
    left: 142px;
    top: 124px;
    font-style: normal;
    font-weight: 700;
    font-size: 44px;
    line-height: 54px;
    color: var(--mint);
  }
  .address {
    position: absolute;
    left: 112px;
    top: 200px;
    font-style: italic;
    font-size: 23px;
    line-height: 32.5px;
  }
  .address-type { display: block; margin-bottom: 25px; }
</style>
</head>
<body>

<section class="card card--front">
  <svg class="frame" width="770" height="592" viewBox="0 0 770 592" aria-hidden="true">
    <path d="M122 58 H648 A70 70 0 0 0 718 128 V470 A70 70 0 0 0 648 540 H122 A70 70 0 0 0 52 470 V128 A70 70 0 0 0 122 58 Z" fill="none" stroke="#fff" stroke-width="2.5"/>
    <path d="M124 65 H646 A65 65 0 0 0 711 130 V468 A65 65 0 0 0 646 533 H124 A65 65 0 0 0 59 468 V130 A65 65 0 0 0 124 65 Z" fill="none" stroke="#fff" stroke-width="1.5"/>
  </svg>
  <div class="ornament" style="left:48px;top:38px" role="img" aria-label="Mint and white curl flourish"></div>
  <div class="ornament" style="left:620px;top:38px" role="img" aria-label="Mint and white curl flourish"></div>
  <div class="ornament" style="left:48px;top:462px" role="img" aria-label="Mint and white curl flourish"></div>
  <div class="ornament" style="left:622px;top:462px" role="img" aria-label="Mint and white curl flourish"></div>

  <ul class="menu-column menu-column--facial">
    <li class="menu-heading">Facial Services:</li>
    <li class="menu-item">Brow Shaping $18</li>
    <li class="menu-item">Lip - $12</li>
    <li class="menu-item">Brow and Lip Combo $25</li>
    <li class="menu-item">Sideburns - $12</li>
    <li class="menu-item">Nose $10</li>
    <li class="menu-item">Ears $10</li>
    <li class="menu-item">Full Face Combo Excluding Brows<br>$40</li>
    <li class="menu-item">Full Face Combo w/ Brow Shaping<br>$55</li>
    <li class="menu-item">Lash Tint $20</li>
    <li class="menu-item">Brow Tint $15</li>
    <li class="menu-note">(This is to darken brows only)</li>
    <li class="menu-item">Brow Shaping + Brow Tint $33</li>
  </ul>

  <ul class="menu-column menu-column--body">
    <li class="menu-heading">Body Waxing :</li>
    <li class="menu-item">Neck $15</li>
    <li class="menu-item">Shoulders$20</li>
    <li class="menu-item">Full back $45</li>
    <li class="menu-item">Chest $45</li>
    <li class="menu-item">(Abdomen Included)</li>
    <li class="menu-item">Abdomen $15</li>
    <li class="menu-item">Underarms $15</li>
    <li class="menu-item">Full Arm $40</li>
    <li class="menu-item">Half Arm $30</li>
    <li class="menu-item">Full Leg $60</li>
    <li class="menu-note menu-note--wrap">(Bikini line not included, This covers<br>the upper thigh down to the feet and toes)</li>
    <li class="menu-item">Half Leg $45</li>
    <li class="menu-item">(Upper or Lower leg)</li>
    <li class="menu-item">Modest Bikini - $35 Female Only</li>
    <li class="menu-item">Brazilian Bikini $55 Female Only</li>
    <li class="menu-item">Buttocks $20</li>
  </ul>
</section>

<section class="card card--back">
  <svg class="frame" width="770" height="594" viewBox="0 0 770 594" aria-hidden="true">
    <path d="M132 60 H638 A70 70 0 0 0 708 130 V460 A70 70 0 0 0 638 530 H132 A70 70 0 0 0 62 460 V130 A70 70 0 0 0 132 60 Z" fill="none" stroke="#fff" stroke-width="2.5"/>
    <path d="M134 67 H636 A65 65 0 0 0 701 132 V458 A65 65 0 0 0 636 523 H134 A65 65 0 0 0 69 458 V132 A65 65 0 0 0 134 67 Z" fill="none" stroke="#fff" stroke-width="1.5"/>
  </svg>
  <div class="ornament" style="left:64px;top:26px" role="img" aria-label="Mint and white curl flourish"></div>
  <div class="ornament" style="left:620px;top:20px" role="img" aria-label="Mint and white curl flourish"></div>
  <div class="ornament" style="left:60px;top:458px" role="img" aria-label="Mint and white curl flourish"></div>
  <div class="ornament" style="left:622px;top:458px" role="img" aria-label="Mint and white curl flourish"></div>

  <h1 class="business-name">Velvet Petal</h1>

  <address class="address">
    <span class="address-type">Waxing Boutique</span>
    Located in Studios Marigo<br>
    415 W. Corbin Dale Blvd<br>
    Suite 17<br>
    Rockwall, TX 75849<br>
    (972)514-2078
  </address>
</section>

</body>
</html>
```